IT Company, Needs new Logo and Letterhead Design

We need a Letterhead and possible a new logo for an existing IT Company. We are not happy with our current Letterhead that we are using in our quotes etc. We are happy to change our logo if required. We will upload our current logo and letterhead and look forward to getting some examples. We provide Server, Workstation and network support.

Target Market(s)

Small to Medium Sized Businesses.

Industry/Entity Type

It Company

Requirements
Must have
• Ability to edit the letterhead at a later date. Will need the source files for editing once approved.
Nice to have
• Same colour scheme, but we are open to suggestions.

```html
<!DOCTYPE html>
<html lang="en">
<head>
<meta charset="utf-8">
<title>Harbourline Network Services – Letterhead</title>
<link rel="stylesheet" href="https://fonts.googleapis.com/css2?family=Oxygen:wght@400&family=Poppins:wght@300&display=swap">
<style>
  :root {
    --navy: #1c2b57;
    --paper: #ffffff;
    --page-edge: #8a8a8a;
    --band-text: #c9cfdf;
  }
  * { margin: 0; padding: 0; box-sizing: border-box; }
  html, body { width: 927px; height: 1200px; overflow: hidden; background: var(--paper); }
  .letterhead {
    position: relative;
    width: 927px;
    height: 1200px;
    background: var(--paper);
    border: 1px solid var(--page-edge);
  }
  .brand {
    position: absolute;
    left: 34px;
    top: 38px;
    display: flex;
    align-items: center;
    gap: 22px;
  }
  .brand-name {
    font-family: "Oxygen", sans-serif;
    font-weight: 400;
    font-size: 41px;
    line-height: 1.08;
    color: var(--navy);
    letter-spacing: -0.5px;
  }
  .brand-mark { width: 26px; height: 26px; border-radius: 50%; background: var(--navy); margin-top: 40px; }
  .side-band {
    position: absolute;
    left: 0;
    top: 206px;
    width: 56px;
    height: 818px;
    background: var(--navy);
  }
  .band-block {
    position: absolute;
    left: 12px;
    writing-mode: vertical-rl;
    transform: rotate(180deg);
    font-family: "Poppins", sans-serif;
    font-weight: 300;
    font-size: 10px;
    line-height: 15px;
    color: var(--band-text);
    white-space: nowrap;
  }
  .band-contact { top: 104px; }
  .band-address { bottom: 32px; }
</style>
</head>
<body>
  <main class="letterhead">
    <header class="brand">
      <div class="brand-name">Harbourline<br>Network Services</div>
      <span class="brand-mark" aria-hidden="true"></span>
    </header>
    <aside class="side-band">
      <p class="band-block band-contact">PHONE: 1300 482 617<br>MOB: 0412 906 238</p>
      <p class="band-block band-address">PO Box 2841, Coral Plaza QLD 4571, 7 Wattle Street Bayview<br>5/2 Banksia Street Elmhurst</p>
    </aside>
  </main>
</body>
</html>
```